Book on emotional dysfunction needs a book cover

This book, entitled "Inner Turmoil and the Scented Memory Path", by Darren Holloway, needs a front cover. The cover could possibly show an adult who is really a child, or a person actively smelling who not really there, like in an alternate dimension.

```html
<!DOCTYPE html>
<html lang="en">
<head>
<meta charset="utf-8">
<title>Inner Turmoil and the Scented Memory Path — Darren Holloway</title>
<link rel="stylesheet" href="https://fonts.googleapis.com/css2?family=Montserrat:wght@700;800;900&display=swap">
<style>
  :root {
    --night-teal: #0f2b37;
    --deep-teal: #0a222d;
    --mustard: #f7c325;
    --band-ink: #12303c;
    --paper-white: #ffffff;
    --shadow: rgba(0, 0, 0, 0.5);
  }
  html, body {
    margin: 0;
    padding: 0;
    overflow: hidden;
    background: var(--deep-teal);
  }
  .cover {
    position: relative;
    width: 777px;
    height: 1200px;
    overflow: hidden;
    background: var(--night-teal);
    font-family: "Montserrat", "Helvetica Neue", Arial, sans-serif;
    text-transform: uppercase;
  }
  .cover__photo {
    position: absolute;
    inset: 0;
    background:
      radial-gradient(ellipse 70px 160px at 350px 60px, rgba(214, 160, 80, 0.55), transparent 75%),
      radial-gradient(ellipse 40px 260px at 400px 420px, rgba(200, 150, 80, 0.45), transparent 75%),
      radial-gradient(ellipse 45px 120px at 445px 740px, rgba(210, 150, 70, 0.5), transparent 75%),
      radial-gradient(ellipse 40px 130px at 480px 880px, rgba(200, 140, 60, 0.4), transparent 75%),
      radial-gradient(ellipse 90px 160px at 740px 1160px, rgba(180, 120, 60, 0.35), transparent 75%),
      radial-gradient(ellipse 170px 110px at 150px 900px, rgba(220, 230, 240, 0.28), transparent 72%),
      radial-gradient(ellipse 90px 60px at 300px 830px, rgba(220, 230, 240, 0.16), transparent 72%),
      linear-gradient(105deg, var(--night-teal) 0%, var(--night-teal) 50%, #0c2530 58%, var(--deep-teal) 100%);
  }
  .title {
    position: absolute;
    inset: 0;
    margin: 0;
    text-align: center;
    font-size: inherit;
  }
  .title > span {
    position: absolute;
    left: 0;
    right: 0;
    line-height: 1;
  }
  .title__lead {
    top: 128px;
    font-size: 66px;
    font-weight: 800;
    color: var(--paper-white);
    text-shadow: 3px 4px 4px var(--shadow);
  }
  .title__band {
    top: 216px;
    height: 75px;
    background: var(--mustard);
    display: flex;
    align-items: center;
    justify-content: center;
    font-size: 56px;
    font-weight: 900;
    color: var(--band-ink);
    letter-spacing: 0.5px;
  }
  .title__link {
    top: 346px;
    font-size: 44px;
    font-weight: 700;
    letter-spacing: 18px;
    padding-left: 18px;
    color: var(--paper-white);
    text-shadow: 3px 3px 3px var(--shadow);
  }
  .title__key {
    top: 396px;
    font-size: 205px;
    font-weight: 800;
    color: var(--mustard);
    text-shadow: 4px 6px 6px var(--shadow);
  }
  .author {
    position: absolute;
    left: 0;
    right: 0;
    top: 1112px;
    margin: 0;
    text-align: center;
    font-size: 44px;
    font-weight: 800;
    line-height: 1;
    letter-spacing: 1px;
    color: var(--paper-white);
    text-shadow: 2px 3px 3px var(--shadow);
  }
</style>
</head>
<body>
  <main class="cover">
    <div class="cover__photo" role="img" aria-label="Dark photograph of a person in profile, the edge of the face lit in warm light, with a thin wisp of smoke drifting from the nose"></div>

    <h1 class="title">
      <span class="title__lead">Inner Turmoil</span>
      <span class="title__band">And the Scented</span>
      <span class="title__link">Memory</span>
      <span class="title__key">Path</span>
    </h1>

    <p class="author">Darren Holloway</p>
  </main>
</body>
</html>
```